National Virtual accounting firm needs website designed

I need a wordpress website design for a national virtual accounting firm. I will upload my business card, logo, and postcards that I have had designed and followed the same style. I want a similar style to be followed so I can keep the running theme similar.

Services include:

Tax Services:
Tax preparation and planning services for Individuals, businesses, estates, and nonprofits
Full Service Payroll for Businesses
ODV Audit Representation

Consulting:
Entity Selection & Restructuring
Financial Projections & Forecasts
Retirement Planning
IPO Readiness

Accounting:
Bookkeeping
Reviews and Compilations
Payroll Services

Other Services:
CFO Services
Compliance Services
Controller Services
Software Implementations for Brimlane, Corvanta, and Plivorn.

Target Market(s)

small to medium size businesses, and individuals

Industry/Entity Type

accounting firms

Font styles to use
Sans Serif

Colors
59FF00
82FF00
B8FF75
E3FFCB
F4FFEA

Requirements
Must have
• Color schematics from the logo and post cards/business cards

```html
<!DOCTYPE html>
<html lang="en">
<head>
<meta charset="utf-8">
<title>Quillan — National Virtual Accounting Firm</title>
<link href="https://fonts.googleapis.com/css2?family=Poppins:wght@400;500;600;700;800&display=swap" rel="stylesheet">
<style>
:root{
  --yellow:#ffc800;
  --green:#4cb13a;
  --green-light:#8cc63f;
  --ink:#1b1b1b;
  --text:#555;
  --mist:#eeeeee;
  --night:#1e1e1e;
  --white:#fff;
}
*{margin:0;padding:0;box-sizing:border-box}
html,body{width:1200px;height:4113px;overflow:hidden}
body{position:relative;font-family:'Poppins',sans-serif;color:var(--ink);background:var(--white)}
.abs{position:absolute}
.btn{position:absolute;background:var(--yellow);color:var(--ink);font-weight:700;font-size:13px;border-radius:30px;display:flex;align-items:center;justify-content:center;text-transform:uppercase}

/* hero */
.hero-photo{position:absolute;left:0;top:0}
.brand{position:absolute;display:flex;align-items:center;gap:10px;font-weight:800;color:var(--white)}
.brand .dot{border-radius:50%;background:var(--yellow)}
.nav{position:absolute;left:479px;top:42px;display:flex;gap:17px;font-size:13px;font-weight:600;color:var(--white)}
.nav .active{color:var(--green-light)}
.menu-toggle{position:absolute;left:1069px;top:31px}
.welcome{position:absolute;left:89px;top:244px;color:var(--white);font-size:26px;font-weight:800}
.welcome::after{content:"";display:block;width:165px;height:3px;background:var(--green-light);border-radius:3px;margin-top:6px}
.hero-title{position:absolute;left:88px;top:300px;color:var(--white);font-size:62px;font-weight:800;line-height:64px}

.section-title{position:absolute;left:0;width:1200px;text-align:center;font-weight:800;font-size:42px;line-height:50px}

/* features */
.feature{position:absolute;width:260px}
.feature h3{font-size:19px;font-weight:700;margin:14px 0 8px}
.feature p{font-size:14px;line-height:21px;color:var(--text)}

/* about */
.about-gray{position:absolute;left:0;top:1640px}
.about-text{position:absolute;left:661px;top:1455px;width:395px}
.about-text h2{font-size:42px;font-weight:800;margin-bottom:8px;line-height:54px}
.about-text p{font-size:13px;line-height:20.5px;color:var(--text)}
.about-text .btn{position:static;width:137px;height:42px;margin-top:20px}

/* services */
.service{position:absolute;width:230px;text-align:center}
.service .ring{width:136px;height:136px;border-radius:50%;border:2px dashed;margin:0 auto;display:flex;align-items:center;justify-content:center}
.service .disc{width:114px;height:114px;border-radius:50%;display:flex;align-items:center;justify-content:center}
.service h3{font-size:18px;font-weight:700;margin:14px 0 4px}
.service p{font-size:14px;line-height:21px;color:var(--text)}

/* consult */
.consult h2{position:absolute;left:204px;top:2400px;font-size:42px;font-weight:800;line-height:45px}
.consult .name{position:absolute;left:206px;top:2502px;font-size:22px;font-weight:600}
.consult .role{position:absolute;left:206px;top:2532px;font-size:15px;color:var(--text)}
.contact-line{position:absolute;left:206px;display:flex;align-items:center;gap:12px;font-size:15px;font-weight:600}

/* blog */
.card{position:absolute;top:2988px;width:274px;min-height:367px;background:var(--white);border-radius:8px;box-shadow:0 8px 24px rgba(0,0,0,.08);overflow:hidden;padding-bottom:22px}
.card .thumb{height:204px}
.card .date{margin:26px 22px 0;font-size:12px;color:var(--green);font-weight:500}
.card h3{margin:6px 22px 0;font-size:16px;font-weight:700;line-height:21px}
.card p{margin:12px 22px 0;font-size:12px;line-height:20px;color:var(--text)}

/* footer */
.footer-col{position:absolute;top:3755px;color:var(--white)}
.footer-col h4{font-size:19px;font-weight:700;margin-bottom:18px}
.footer-col li{list-style:none;font-size:13px;line-height:31px}
.footer-col li::before{content:"›";margin-right:8px}
.contact-item{display:flex;gap:10px;font-size:13px;line-height:18px;margin-bottom:16px}
.socials{display:flex;gap:8px}
.socials span{width:26px;height:26px;border-radius:50%;background:var(--white);display:block}
.copyright{position:absolute;left:0;top:4072px;width:1200px;text-align:center;color:var(--white);font-size:12px;font-weight:600}
</style>
</head>
<body>

<!-- hero -->
<svg class="hero-photo" width="1200" height="880" viewBox="0 0 1200 880" role="img" aria-label="Photo of two accountants in an office reviewing work on a laptop">
  <defs>
    <linearGradient id="heroTone" x1="0" y1="0" x2="1" y2="1">
      <stop offset="0" stop-color="#4a4f57"/>
      <stop offset=".5" stop-color="#6f6a63"/>
      <stop offset="1" stop-color="#a78867"/>
    </linearGradient>
  </defs>
  <path d="M0,0H1200V728C1120,742 1020,640 900,640C720,640 610,872 340,872C160,872 60,810 0,762Z" fill="url(#heroTone)"/>
  <path d="M0,0H1200V728C1120,742 1020,640 900,640C720,640 610,872 340,872C160,872 60,810 0,762Z" fill="rgba(0,0,0,.28)"/>
</svg>

<div class="brand" style="left:90px;top:30px;font-size:32px"><span class="dot" style="width:22px;height:22px"></span>QUILLAN</div>
<nav class="nav"><span class="active">Home</span><span>About Us</span><span>Services</span><span>Testimonial</span><span>Blog</span><span>Contact</span></nav>
<div class="btn" style="left:903px;top:32px;width:155px;height:40px;font-size:12px">Book a Meeting</div>
<svg class="menu-toggle" width="42" height="42" viewBox="0 0 42 42"><circle cx="21" cy="21" r="20" fill="#fff"/><path d="M13 16h16M15 21h14M13 26h16" stroke="#1b1b1b" stroke-width="2" stroke-linecap="round"/></svg>

<div class="welcome">Welcome To</div>
<h1 class="hero-title">National Virtual<br>Accounting<br>Firm</h1>
<div class="btn" style="left:88px;top:512px;width:202px;height:42px;font-size:12px">Let,s Work Togather</div>

<!-- intro -->
<h2 class="section-title" style="top:940px">When Your Finances<br>Could be Quillan?</h2>

<div class="feature" style="left:88px;top:1092px">
  <svg width="66" height="66" viewBox="0 0 66 66" fill="none" stroke="#4cb13a" stroke-width="2.5"><rect x="4" y="4" width="42" height="56" rx="2"/><path d="M12 18h26M12 28h26M12 38h18M12 48h14"/><path d="M56 22l6 6-22 24-8 2 2-8z"/></svg>
  <h3>Bookkeeping</h3>
  <p>take the hassle out of managing your finances with our professional bookkeeping services.</p>
</div>
<div class="feature" style="left:463px;top:1092px">
  <svg width="66" height="66" viewBox="0 0 66 66" fill="none" stroke="#4cb13a" stroke-width="2.5"><path d="M16 6h44v50a6 6 0 0 1-6 6H10a6 6 0 0 1-6-6V44h12z"/><path d="M28 18h24M28 28h24M28 38h24"/><circle cx="14" cy="26" r="9"/><path d="M10 30l8-8"/></svg>
  <h3>Taxes</h3>
  <p>Expert guidance, maximum refunds, timely filing, and peace of mind. our tax services are reliable for both in-dividuals and businesses</p>
</div>
<div class="feature" style="left:849px;top:1092px">
  <svg width="66" height="66" viewBox="0 0 66 66" fill="none" stroke="#4cb13a" stroke-width="2.5"><circle cx="33" cy="8" r="6"/><circle cx="10" cy="33" r="6"/><circle cx="56" cy="33" r="6"/><circle cx="33" cy="58" r="6"/><circle cx="33" cy="28" r="6"/><path d="M22 46c0-7 5-11 11-11s11 4 11 11z"/><path d="M14 27l12-14M52 27L40 13M14 39l12 14M52 39L40 53"/></svg>
  <h3>Full service payroll</h3>
  <p>trreamline your payroll our reliable services. accurate calculations, timely payments, and expert tax compliance</p>
</div>

<!-- about -->
<svg class="about-gray" width="1200" height="270" viewBox="0 0 1200 270">
  <path d="M0,150C90,60 200,30 330,80C500,150 620,262 840,266C1020,268 1140,210 1200,170V270H0Z" fill="#eee"/>
</svg>

<svg class="abs" style="left:159px;top:1376px" width="448" height="448" viewBox="0 0 448 448" role="img" aria-label="Photo of a team meeting around a round table with laptops">
  <defs><linearGradient id="aboutTone" x1="0" y1="0" x2="1" y2="1"><stop offset="0" stop-color="#d9d6d0"/><stop offset=".55" stop-color="#8d8780"/><stop offset="1" stop-color="#e6e3df"/></linearGradient></defs>
  <circle cx="224" cy="224" r="224" fill="url(#aboutTone)"/>
</svg>

<div class="about-text">
  <h2>About Quillan?</h2>
  <p>It is a long established fact that a reader will be distracted by the readable content of a page when looking at its layout. The point of using Lorem Ipsum is that it has a more-or-less normal distribution of letters, as opposed to using 'Content here, content here', making it look like readable English. Many desktop publishing packages and web page editors now use Lorem Ipsum as their default model text, and a search for 'lorem ipsum' will uncover</p>
  <div class="btn">Read More</div>
</div>

<!-- services -->
<h2 class="section-title" style="top:1914px">High Quality Services</h2>

<div class="service" style="left:96px;top:2004px">
  <div class="ring" style="border-color:var(--yellow)"><div class="disc" style="background:var(--yellow)">
    <svg width="54" height="54" viewBox="0 0 54 54" fill="none" stroke="#fff" stroke-width="2.2"><path d="M10 4h24l10 10v36H10z"/><path d="M16 14h12M16 22h22M16 30h22"/><circle cx="20" cy="42" r="7"/><path d="M17 42l2 2 4-4"/></svg>
  </div></div>
  <h3>Tax</h3><p>Tax preparation and plan-ning services for Individuals, businesses,...</p>
</div>
<div class="service" style="left:354px;top:2004px">
  <div class="ring" style="border-color:var(--green)"><div class="disc" style="background:var(--green)">
    <svg width="54" height="54" viewBox="0 0 54 54" fill="none" stroke="#fff" stroke-width="2.2"><circle cx="18" cy="22" r="7"/><path d="M4 46c0-9 6-14 14-14s14 5 14 14z"/><path d="M32 28V16M38 28V10M44 28V18M50 28V6"/><path d="M30 30h22"/></svg>
  </div></div>
  <h3>Consulting</h3><p>Entity Selection &amp; Restructur-ing Financial Projections &amp; Forecasts...</p>
</div>
<div class="service" style="left:614px;top:2004px">
  <div class="ring" style="border-color:var(--green)"><div class="disc" style="background:var(--green)">
    <svg width="54" height="54" viewBox="0 0 54 54" fill="none" stroke="#fff" stroke-width="2.2"><rect x="6" y="4" width="26" height="38" rx="2"/><path d="M11 10h16v8H11zM11 24h4M19 24h4M11 31h4M19 31h4"/><path d="M30 20h14l6 6v24H24V38"/><circle cx="38" cy="38" r="6"/></svg>
  </div></div>
  <h3>Accounting</h3><p>Bookkeeping Reviews and Compilations Payroll Services</p>
</div>
<div class="service" style="left:876px;top:2004px">
  <div class="ring" style="border-color:var(--green-light)"><div class="disc" style="background:var(--green-light)">
    <svg width="54" height="54" viewBox="0 0 54 54" fill="none" stroke="#fff" stroke-width="2.2"><circle cx="30" cy="18" r="10"/><circle cx="30" cy="18" r="4"/><path d="M4 36h8l10 4h12a3 3 0 0 1 0 6H22"/><path d="M12 50l14 0 20-10a3 3 0 0 0-3-5l-9 4"/></svg>
  </div></div>
  <h3>Additional Services</h3><p>CFO Services Compliance Services Controller Services Software...</p>
</div>

<!-- consult -->
<section class="consult">
  <h2>Shedule A Free<br>Consult Now</h2>
  <div class="name">Daniel M. Hartwell, CPA</div>
  <div class="role">Founder/Owner</div>
  <div class="contact-line" style="top:2576px"><svg width="18" height="18" viewBox="0 0 24 24"><path d="M6 2l4 4-2 3c1 3 4 6 7 7l3-2 4 4-3 4C10 22 2 14 2 5z" fill="#4cb13a"/></svg>(555) 410-2286</div>
  <div class="contact-line" style="top:2611px"><svg width="18" height="18" viewBox="0 0 24 24" fill="#4cb13a"><rect x="6" y="2" width="12" height="6"/><rect x="2" y="9" width="20" height="9" rx="2"/><rect x="6" y="15" width="12" height="7" fill="#fff" stroke="#4cb13a" stroke-width="2"/></svg>(555) 732-0914</div>
  <div class="contact-line" style="top:2646px"><svg width="18" height="18" viewBox="0 0 24 24"><rect x="2" y="5" width="20" height="14" rx="1" fill="#4cb13a"/><path d="M2 6l10 7 10-7" stroke="#fff" stroke-width="2" fill="none"/></svg>daniel@quillan.com</div>
  <div class="contact-line" style="top:2682px"><svg width="18" height="18" viewBox="0 0 24 24" fill="none" stroke="#4cb13a" stroke-width="2"><circle cx="12" cy="12" r="9"/><path d="M3 12h18M12 3c4 4 4 14 0 18M12 3c-4 4-4 14 0 18"/></svg>www.quillan.com</div>
  <div class="btn" style="left:206px;top:2733px;width:141px;height:44px">Contact Us</div>
</section>
<svg class="abs" style="left:598px;top:2385px" width="400" height="410" viewBox="0 0 400 410" role="img" aria-label="Photo of two young clients looking at a smartphone together">
  <defs><linearGradient id="consultTone" x1="0" y1="0" x2="1" y2="1"><stop offset="0" stop-color="#b88a6c"/><stop offset=".5" stop-color="#7b5a45"/><stop offset="1" stop-color="#d9a878"/></linearGradient></defs>
  <circle cx="200" cy="208" r="200" fill="url(#consultTone)"/>
</svg>

<!-- blog -->
<h2 class="section-title" style="top:2915px">Latest Blog</h2>
<article class="card" style="left:171px">
  <div class="thumb" role="img" aria-label="Photo of two colleagues discussing charts at a desk" style="background:linear-gradient(135deg,#cfd6d4,#5e5a58)"></div>
  <div class="date">18-07-2023</div><h3>Some event heading<br>goes here</h3><p>Aenean sollicitudin lorem bibendum auctor nisi elit consequat ipsum...</p>
</article>
<article class="card" style="left:463px">
  <div class="thumb" role="img" aria-label="Photo of a business team reviewing a tablet" style="background:linear-gradient(135deg,#9a958c,#4c4843)"></div>
  <div class="date">18-07-2023</div><h3>Some event heading<br>goes here</h3><p>Aenean sollicitudin lorem bibendum auctor nisi elit consequat ipsum...</p>
</article>
<article class="card" style="left:755px">
  <div class="thumb" role="img" aria-label="Photo of colleagues talking in a bright office" style="background:linear-gradient(135deg,#e4e4e2,#7a7775)"></div>
  <div class="date">18-07-2023</div><h3>Some event heading<br>goes here</h3><p>Aenean sollicitudin lorem bibendum auctor nisi elit consequat ipsum...</p>
</article>

<!-- footer -->
<svg class="abs" style="left:0;top:3490px" width="1200" height="623" viewBox="0 0 1200 623">
  <path d="M0,270C150,100 380,20 600,20C830,20 1060,110 1200,260V623H0Z" fill="#ffc800"/>
  <path d="M0,300C150,130 380,48 600,48C830,48 1060,140 1200,290V623H0Z" fill="#1e1e1e"/>
</svg>
<div class="brand" style="left:0;width:1200px;justify-content:center;top:3610px;font-size:66px;gap:16px"><span class="dot" style="width:34px;height:34px"></span>QUILLAN</div>

<div class="footer-col" style="left:192px">
  <h4>Quick Links</h4>
  <ul><li>Home</li><li>About Us</li><li>Services</li><li>Testimonial</li><li>Blog</li><li>Contact</li></ul>
</div>
<div class="footer-col" style="left:433px">
  <h4>Services</h4>
  <ul><li>Tax</li><li>Consulting</li><li>Accounting</li><li>Additional Services</li></ul>
</div>
<div class="footer-col" style="left:635px">
  <h4>Contact Info</h4>
  <div class="contact-item"><svg width="14" height="14" viewBox="0 0 24 24"><rect x="2" y="5" width="20" height="14" fill="#4cb13a"/><path d="M2 6l10 7 10-7" stroke="#1e1e1e" stroke-width="2" fill="none"/></svg><div>Email:<br>daniel@quillan.com</div></div>
  <div class="contact-item"><svg width="14" height="14" viewBox="0 0 24 24"><path d="M6 2l4 4-2 3c1 3 4 6 7 7l3-2 4 4-3 4C10 22 2 14 2 5z" fill="#4cb13a"/></svg><div>Phone:<br>(555) 410-2286</div></div>
  <div class="contact-item"><svg width="14" height="14" viewBox="0 0 24 24"><path d="M12 2a7 7 0 0 0-7 7c0 5 7 13 7 13s7-8 7-13a7 7 0 0 0-7-7z" fill="#4cb13a"/><circle cx="12" cy="9" r="2.5" fill="#1e1e1e"/></svg><div>Web:<br>www.quillan.com</div></div>
</div>
<div class="footer-col" style="left:884px">
  <h4>Follow Us</h4>
  <div class="socials"><span></span><span></span><span></span><span></span></div>
</div>

<svg class="abs" style="left:1129px;top:4029px" width="44" height="44" viewBox="0 0 44 44"><circle cx="22" cy="22" r="21" fill="#4cb13a"/><path d="M22 30V14M16 20l6-6 6 6" stroke="#fff" stroke-width="2" fill="none" stroke-linecap="round"/></svg>
<div class="copyright">© Copyright 2023, All Rights Reserved</div>

</body>
</html>
```